Online Shop Marta

We need a web design for an online shop, called "Orvil Dapt Jewels". The shop should have an extraordinary, elegant look, as shown in the Quincefield Advertising Picture in our Briefing.pdf (attached). Please have a look at our Briefing regarding website colours, background ideas, and elements to be included. The online shop is about professional jewellery design pieces, where each piece is handmade of high quality materials, also unique pieces and unique editions possible. It should attract extraordinary people and visualize that its a very individual and unique design jewellery. You can get an idea of whom it should attract by reading our target group. Colours to be used are jewellery-Velvet red, Black / anthracite, exclusive colours, silverish-white, bronze-brown and golden.

Please play around when designing with the image pictures we attach, preferably more vertical pictures, no panoramic pictures like in Brontel Shop. Also include the BLACK logo of orvil dapt. We include the SITEMAP in the briefing and also another folder with product pictures you can use for the draft.

Regarding Functions, the store will have the SAME (technical) functions as this page:http://www.brontel-shop.eu/ - using the "most famous" products/categories for the starting page, going into individual product pages by clicking these images and then leading to a detailed page for one product only.

Target Market(s)

Jewellery-lovers, who appreciate extraordinary things, creative economy/fashion-industries, stylists, Style consultants, outfitter, theatres, operas, production sites, Cocktail-, Dinner and Bridefashion, exclusive traditional costume stores, dancesports and tango argento dancers

Industry/Entity Type

Shop

Requirements
Must have
• Must include:
• Colours as per briefing
• Background ideas/images as per briefing/pictures sent
• Sitemap as per briefing
• Social buttons
• Logo
• Design for 3 pages: Starting page showing big images, attractive design and the 4 popular categories
• Subpage with different products of one category (i.e. bracelets)
• Detail page with one individual product only
Should not have
• no fresh, playful colours like yellow, orange, green, blue
• no cheap design, no panorama pictures

```html
<!DOCTYPE html>
<html lang="en">
<head>
<meta charset="utf-8">
<title>Orvil Dapt Jewels – Online Shop</title>
<link rel="stylesheet" href="https://fonts.googleapis.com/css2?family=Cinzel:wght@400;700&family=Open+Sans:wght@400;600&family=Ubuntu:wght@300;400&display=swap">
<style>
:root{
  --page:#1c1c1c;
  --wood-dark:#1a1512;
  --wood-mid:#2b231e;
  --gold:#f2c54d;
  --gold-deep:#d9a52c;
  --ink:#2a1e10;
  --text:#e8e8e8;
  --muted:#a9a9a9;
  --line:#3a3a3a;
  --frame:#555555;
  --panel:#222222;
  --thumb-base:#343436;
}
*{margin:0;padding:0;box-sizing:border-box}
html,body{width:779px;height:1200px;overflow:hidden}
body{position:relative;background:var(--page);font-family:"Open Sans",sans-serif;color:var(--text)}
h1,h2{font:inherit}
.abs{position:absolute}

.wood-band{left:0;top:0;width:779px;height:300px;
  background:repeating-linear-gradient(90deg,rgba(0,0,0,.18) 0 2px,rgba(0,0,0,0) 2px 46px),
  linear-gradient(90deg,var(--wood-dark) 0%,var(--wood-mid) 18%,#231c18 35%,var(--wood-mid) 55%,#201a16 75%,var(--wood-mid) 100%);}
.wood-fade{left:0;top:240px;width:779px;height:60px;background:linear-gradient(180deg,rgba(28,28,28,0),var(--page))}

.brand{left:0;top:20px;width:779px;text-align:center;font-family:"Ubuntu",sans-serif;font-weight:400;color:#f4f4f4}
.brand-name{font-size:32px;line-height:40px;letter-spacing:.5px}
.brand-tag{font-size:17px;line-height:22px;margin-top:2px}

.social{left:70px;top:65px;display:flex;gap:2px}
.social span{width:18px;height:18px;border-radius:50%;background:#f4f4f4;display:block}

.cart{left:634px;top:25px;width:73px;height:25px;border:1px solid #4a4a4a;border-radius:13px;background:#151515;
  display:flex;align-items:center;justify-content:center;gap:4px;font-family:"Ubuntu",sans-serif;font-size:10px;color:#eee}
.search{left:554px;top:65px;width:157px;height:21px;border:1px solid #4a4a4a;background:#141414;
  font-size:8px;font-style:italic;color:#aaa;padding:0 8px;display:flex;align-items:center;justify-content:space-between}

.main-nav{left:66px;top:97px;width:647px;height:31px;background:linear-gradient(180deg,#f7d267,var(--gold-deep));
  display:flex;align-items:center;justify-content:center;gap:14px;font-family:"Cinzel",serif;font-size:12px;color:var(--ink);letter-spacing:.3px}
.main-nav .dia{font-size:8px}

.hero{left:66px;top:128px;width:647px;height:179px;border:1px solid #555;
  background:
  radial-gradient(ellipse 120px 110px at 52% 100%,#e9e6e1 0%,#bdb7b0 45%,rgba(120,115,112,0) 100%),
  linear-gradient(180deg,rgba(0,0,0,0) 0%,rgba(0,0,0,.25) 100%),
  linear-gradient(90deg,#2e3340 0%,#4a4f60 18%,#6b6470 36%,#4a3b38 48%,#57525a 60%,#2d3b52 76%,#3e536e 90%,#2a3446 100%);}
.hero-title{left:66px;top:180px;width:647px;text-align:center;font-family:"Cinzel",serif;font-weight:700;font-size:28px;line-height:34px;
  color:#f6e7bd;text-shadow:0 0 2px #000,0 1px 6px rgba(0,0,0,.9)}

.side-heading{font-size:11.5px;letter-spacing:.3px;color:var(--text);font-weight:400}
.categories{left:70px;top:336px;width:152px}
.categories h2{padding-bottom:6px;border-bottom:1px solid var(--line)}
.categories ul{list-style:none;margin-top:5px}
.categories li{font-size:8px;height:17.5px;line-height:16px;border-bottom:1px solid #2c2c2c;padding-left:4px;display:flex;gap:10px}
.categories li:last-child{border-bottom:none}
.chev{color:#888}

.shop-list-head{left:68px;top:451px;width:140px;display:flex;justify-content:space-between;align-items:center;color:var(--gold);font-size:11.5px}
.arrows{color:#bbb;font-size:13px;letter-spacing:2px;line-height:1}
.shop-list{left:67px;top:474px;width:142px;height:208px;border:1px solid #444;background:var(--panel)}
.shop-list .name{position:absolute;left:12px;top:10px;font-size:8.5px;font-weight:600}
.shop-list .thumb{position:absolute;left:12px;top:26px;width:119px;height:144px;
  background:radial-gradient(ellipse 40px 70px at 60% 48%,#9a948c 0%,#5c5853 45%,#222 100%)}
.price-badge{position:absolute;left:19px;top:116px;width:36px;height:36px;border-radius:50%;background:#fff;color:#222;
  font-family:"Ubuntu",sans-serif;font-size:12.5px;display:flex;align-items:center;justify-content:center}
.shop-list .btn{position:absolute;left:11px;top:178px;width:61px;height:15px;background:#f2f2f2;color:#444;font-size:7px;
  display:flex;align-items:center;justify-content:center;border:1px solid #999}

.products-head{left:254px;top:333px;width:444px;height:18px;border-bottom:1px solid var(--line);display:flex;justify-content:space-between}

.product-grid{display:grid;grid-template-columns:repeat(3,141px);column-gap:11px;row-gap:11px}
.grid-a{left:254px;top:363px}
.grid-b{left:262px;top:714px}
.product{position:relative;width:141px;height:167px}
.product .thumb{width:141px;height:131px;border:1px solid var(--frame);border-radius:2px}
.product .meta{position:absolute;left:0;top:146px;width:141px;height:18px;display:flex;align-items:center}
.product .meta svg{margin:0 6px 0 0}
.info-btn{width:58px;height:14px;background:linear-gradient(180deg,#f6cd5c,var(--gold-deep));color:#4a3410;font-size:7px;
  display:flex;align-items:center;justify-content:center}
.price{margin-left:auto;font-family:"Ubuntu",sans-serif;font-weight:300;font-size:11px;color:var(--muted)}

.t-silver{background:linear-gradient(160deg,#c9c9c9 0%,#8b8b8d 40%,#4a4a4c 75%,#333 100%)}
.t-silvergold{background:linear-gradient(160deg,#cfc3ae 0%,#9a8c76 40%,#514b44 75%,#353333 100%)}
.t-gold{background:linear-gradient(160deg,#5a5550 0%,#7c6433 45%,#4a4035 75%,#333 100%)}
.t-black{background:linear-gradient(160deg,#4d4d50 0%,#2a2a2d 45%,#141416 75%,#2e2e30 100%)}
.t-blackbust{background:linear-gradient(180deg,#5a5a5c 0%,#3a3a3c 45%,#151517 80%,#262628 100%)}
.t-pearl{background:linear-gradient(180deg,#3d3d40 0%,#5e5c58 35%,#d9d4c9 55%,#6a6760 70%,#3a3a3c 100%)}
.t-goldpanel{background:linear-gradient(90deg,#222 0%,#5b5e63 22%,#b39540 40%,#caa84a 50%,#b39540 60%,#5b5e63 78%,#222 100%)}
.t-earring{background:linear-gradient(90deg,#222 0%,#3b3a38 20%,#8d877e 40%,#4a4845 55%,#9a948a 70%,#2a2a2a 100%)}
.t-ring{background:linear-gradient(160deg,#333 0%,#555456 30%,#b9b4a6 50%,#6a665c 70%,#3a3a3c 100%)}
.t-bracelet{background:linear-gradient(150deg,#a9a7a3 0%,#d6d3cd 35%,#8b8883 60%,#3c3c3e 100%)}
.t-pendant{background:linear-gradient(90deg,#1e1e1e 0%,#2e2e2e 28%,#8b857c 48%,#6e6455 58%,#2a2a2a 75%,#1e1e1e 100%)}
.t-bronze{background:linear-gradient(160deg,#3a3837 0%,#56524e 30%,#8a6c45 55%,#4f4032 75%,#2c2b2b 100%)}

.pager{left:438px;top:1069px;display:flex;align-items:center}
.pager span{height:16px;border:1px solid #666;background:#151515;color:#ddd;font-size:7px;font-weight:600;
  display:flex;align-items:center;justify-content:center;position:absolute;top:0}
.pager .on{background:var(--gold);color:#222;border-color:var(--gold)}
.pager .gap{border:none;background:none;color:#888;top:3px}

.footer-line{left:66px;top:1112px;width:647px;height:1px;background:var(--line)}
.footer-nav{left:68px;top:1138px;font-family:"Ubuntu",sans-serif;font-size:9.5px;color:#ddd;display:flex;gap:5px}
.footer-nav .sep{color:#888}
.copyright{left:68px;top:1159px;font-size:7px;color:#777}
.payments{left:582px;top:1138px;display:flex;gap:4px}
.payments span{width:27px;height:18px;border-radius:2px;background:#e6e6e6;display:block}
</style>
</head>
<body>

<div class="abs wood-band" role="img" aria-label="Dark wooden plank background"></div>
<div class="abs wood-fade"></div>

<header>
  <div class="abs brand">
    <div class="brand-name">Orvil Dapt</div>
    <div class="brand-tag">♦ Jewels ♦</div>
  </div>
  <div class="abs social" aria-label="Social links"><span></span><span></span><span></span><span></span></div>
  <div class="abs cart">My Cart
    <svg width="16" height="14" viewBox="0 0 16 14" fill="none" stroke="#eee" stroke-width="1.3"><path d="M1 1h2.5l2 8h7.5l1.5-5.5H4.5"/><circle cx="6.5" cy="12" r="1"/><circle cx="12" cy="12" r="1"/></svg>
  </div>
  <div class="abs search">Search here..
    <svg width="11" height="11" viewBox="0 0 11 11" fill="none" stroke="#eee" stroke-width="1.5"><circle cx="4.5" cy="4.5" r="3.5"/><path d="M7 7l3 3"/></svg>
  </div>
  <nav class="abs main-nav">
    <span>HOME</span><span class="dia">♦</span><span>ONLINE SHOP</span><span class="dia">♦</span><span>INFO &amp; FACTS</span><span class="dia">♦</span><span>PARTNER</span><span class="dia">♦</span><span>ABOUT ME</span><span class="dia">♦</span><span>CONTACT</span>
  </nav>
</header>

<section>
  <div class="abs hero" role="img" aria-label="Photo of a woman in a white coat wearing a crystal necklace on a city street"></div>
  <h1 class="abs hero-title">A DREAM JEWELLERY<br>COLLECTION HERE..</h1>
</section>

<aside>
  <div class="abs categories">
    <h2 class="side-heading">CATEGORIES</h2>
    <ul>
      <li><span class="chev">›</span>Collier</li>
      <li><span class="chev">›</span>Bracelet</li>
      <li><span class="chev">›</span>Ring</li>
      <li><span class="chev">›</span>Earring</li>
    </ul>
  </div>
  <div class="abs shop-list-head"><h2>SHOPPING LIST</h2><span class="arrows">‹›</span></div>
  <div class="abs shop-list">
    <div class="name">Anhänger</div>
    <div class="thumb" role="img" aria-label="Beaded silver and bronze pendant with tassel on a wire"></div>
    <div class="price-badge">275€</div>
    <div class="btn">Product Info</div>
  </div>
</aside>

<main>
  <div class="abs products-head"><h2 class="side-heading">PRODUCTS</h2><span class="arrows">‹›</span></div>

  <div class="abs product-grid grid-a">
    <div class="product"><div class="thumb t-silver" role="img" aria-label="Silver crystal net collier"></div><div class="meta"><svg width="11" height="9" viewBox="0 0 11 9"><path d="M0 3h11l-1.5 6h-8z" fill="#888"/><path d="M3 3l2.5-3 2.5 3" stroke="#888" fill="none"/></svg><span class="info-btn">Product Info</span><span class="price">Collier 55 €</span></div></div>
    <div class="product"><div class="thumb t-silvergold" role="img" aria-label="Silver and champagne beaded collar collier"></div><div class="meta"><svg width="11" height="9" viewBox="0 0 11 9"><path d="M0 3h11l-1.5 6h-8z" fill="#888"/><path d="M3 3l2.5-3 2.5 3" stroke="#888" fill="none"/></svg><span class="info-btn">Product Info</span><span class="price">Collier 55 €</span></div></div>
    <div class="product"><div class="thumb t-gold" role="img" aria-label="Gold beaded collier with diamond-shaped drops"></div><div class="meta"><svg width="11" height="9" viewBox="0 0 11 9"><path d="M0 3h11l-1.5 6h-8z" fill="#888"/><path d="M3 3l2.5-3 2.5 3" stroke="#888" fill="none"/></svg><span class="info-btn">Product Info</span><span class="price">Collier 55 €</span></div></div>
    <div class="product"><div class="thumb t-black" role="img" aria-label="Black beaded choker collier"></div><div class="meta"><svg width="11" height="9" viewBox="0 0 11 9"><path d="M0 3h11l-1.5 6h-8z" fill="#888"/><path d="M3 3l2.5-3 2.5 3" stroke="#888" fill="none"/></svg><span class="info-btn">Product Info</span><span class="price">Collier 55 €</span></div></div>
    <div class="product"><div class="thumb t-blackbust" role="img" aria-label="Black crystal net collier on display bust"></div><div class="meta"><svg width="11" height="9" viewBox="0 0 11 9"><path d="M0 3h11l-1.5 6h-8z" fill="#888"/><path d="M3 3l2.5-3 2.5 3" stroke="#888" fill="none"/></svg><span class="info-btn">Product Info</span><span class="price">Collier 55 €</span></div></div>
    <div class="product"><div class="thumb t-pearl" role="img" aria-label="Large pearls with gold accents on a wire"></div><div class="meta"><svg width="11" height="9" viewBox="0 0 11 9"><path d="M0 3h11l-1.5 6h-8z" fill="#888"/><path d="M3 3l2.5-3 2.5 3" stroke="#888" fill="none"/></svg><span class="info-btn">Product Info</span><span class="price">Collier 55 €</span></div></div>
  </div>

  <div class="abs product-grid grid-b">
    <div class="product"><div class="thumb t-goldpanel" role="img" aria-label="Gold woven pendant on a wire"></div><div class="meta"><svg width="11" height="9" viewBox="0 0 11 9"><path d="M0 3h11l-1.5 6h-8z" fill="#888"/><path d="M3 3l2.5-3 2.5 3" stroke="#888" fill="none"/></svg><span class="info-btn">Product Info</span><span class="price">Collier 55 €</span></div></div>
    <div class="product"><div class="thumb t-earring" role="img" aria-label="Pair of crescent beaded earrings"></div><div class="meta"><svg width="11" height="9" viewBox="0 0 11 9"><path d="M0 3h11l-1.5 6h-8z" fill="#888"/><path d="M3 3l2.5-3 2.5 3" stroke="#888" fill="none"/></svg><span class="info-btn">Product Info</span><span class="price">Collier 55 €</span></div></div>
    <div class="product"><div class="thumb t-ring" role="img" aria-label="Crystal beaded ring"></div><div class="meta"><svg width="11" height="9" viewBox="0 0 11 9"><path d="M0 3h11l-1.5 6h-8z" fill="#888"/><path d="M3 3l2.5-3 2.5 3" stroke="#888" fill="none"/></svg><span class="info-btn">Product Info</span><span class="price">Collier 55 €</span></div></div>
    <div class="product"><div class="thumb t-bracelet" role="img" aria-label="Two crystal beaded bracelets"></div><div class="meta"><svg width="11" height="9" viewBox="0 0 11 9"><path d="M0 3h11l-1.5 6h-8z" fill="#888"/><path d="M3 3l2.5-3 2.5 3" stroke="#888" fill="none"/></svg><span class="info-btn">Product Info</span><span class="price">Collier 55 €</span></div></div>
    <div class="product"><div class="thumb t-pendant" role="img" aria-label="Silver and bronze beaded pendant"></div><div class="meta"><svg width="11" height="9" viewBox="0 0 11 9"><path d="M0 3h11l-1.5 6h-8z" fill="#888"/><path d="M3 3l2.5-3 2.5 3" stroke="#888" fill="none"/></svg><span class="info-btn">Product Info</span><span class="price">Collier 55 €</span></div></div>
    <div class="product"><div class="thumb t-bronze" role="img" aria-label="Bronze beaded pendant on a wire"></div><div class="meta"><svg width="11" height="9" viewBox="0 0 11 9"><path d="M0 3h11l-1.5 6h-8z" fill="#888"/><path d="M3 3l2.5-3 2.5 3" stroke="#888" fill="none"/></svg><span class="info-btn">Product Info</span><span class="price">Collier 55 €</span></div></div>
  </div>

  <div class="abs pager" aria-label="Pagination">
    <span style="left:0;width:16px">‹</span>
    <span style="left:24px;width:16px">1</span>
    <span style="left:48px;width:16px">2</span>
    <span style="left:72px;width:16px">3</span>
    <span class="on" style="left:96px;width:16px">4</span>
    <span style="left:120px;width:16px">5</span>
    <span class="gap" style="left:146px;width:14px">.....</span>
    <span style="left:168px;width:18px">15</span>
    <span style="left:192px;width:18px">30</span>
    <span style="left:218px;width:18px">45</span>
    <span style="left:244px;width:16px">›</span>
  </div>
</main>

<footer>
  <div class="abs footer-line"></div>
  <nav class="abs footer-nav">
    <span>Home</span><span class="sep">|</span><span>Online Shop</span><span class="sep">|</span><span>Info &amp; Facts</span><span class="sep">|</span><span>Partner</span><span class="sep">|</span><span>About me</span><span class="sep">|</span><span>Contact</span>
  </nav>
  <div class="abs copyright">© 2013 Company Name. All right reserved</div>
  <div class="abs payments" aria-label="Accepted payment cards"><span></span><span></span><span></span><span></span></div>
</footer>

</body>
</html>
```